Website Monitoring Business Needs a Single Page Website Design

I need a website design for a new web based service called LoopWatch. This service checks to see if a website is up or down and how quickly or slowly it is responding. Users sign up for a small monthly fee and add one or more websites to monitor based on the plan they purchase. I prefer a single page design.

There will be 3 pricing plans to start with. A free plan and then 2 paid plans. The pricing plans should be included on the single page.

Here are four close competitors to what this product will offer:

https://www.zentrovia.com/
http://haldersync.com/
https://www.brimolux.com/
https://www.quorvane5.com/

Target Market(s)

Website owners, bloggers

Industry/Entity Type

Business

Coding

Coded - Design and coding required

Number of Pages Required

1 page

Font styles to use
Sans Serif

Requirements
Must have
• Responsive design
Nice to have
• Parallax scrolling

```html
<!DOCTYPE html>
<html lang="en">
<head>
<meta charset="utf-8">
<title>LoopWatch — Website monitoring for everyone</title>
<link rel="stylesheet" href="https://fonts.googleapis.com/css2?family=Open+Sans:ital,wght@0,400;0,600;0,700;1,400&display=swap">
<style>
:root{
  --orange:#f06a24;
  --dark:#2b2b2e;
  --darker:#242427;
  --ink:#2e2e2e;
  --muted:#6f6f6f;
  --light:#e9e9e9;
  --white:#ffffff;
  --free:#f7a81b;
  --standard:#2aa89c;
  --premium:#5bb5e2;
  --teal:#34b2b8;
}
*{box-sizing:border-box;margin:0;padding:0}
html,body{width:1200px;height:4110px;overflow:hidden}
body{font-family:"Open Sans",Arial,sans-serif;color:var(--ink);background:var(--white);position:relative}
section,header,footer{position:relative;width:1200px}
.section-title{text-align:center;font-size:33px;font-weight:600;color:var(--ink)}
.section-sub{text-align:center;font-size:14px;color:var(--muted);margin-top:10px}

/* Hero */
.hero{height:690px;overflow:hidden;color:var(--white)}
.hero-photo{position:absolute;inset:0;background:linear-gradient(120deg,#6b6258 0%,#3f3c3a 40%,#55585c 70%,#2f3033 100%)}
.hero-shade{position:absolute;inset:0;background:rgba(20,20,22,.35)}
.nav{position:absolute;top:46px;left:62px;right:62px;display:flex;justify-content:space-between;align-items:center}
.brand{font-size:34px;font-weight:700;color:var(--white);letter-spacing:-.5px}
.nav-links{display:flex;gap:48px;list-style:none;font-size:12px;font-weight:700;letter-spacing:.3px}
.hero-dots{position:absolute;right:48px;top:268px;display:flex;flex-direction:column;gap:14px}
.hero-dots span{width:8px;height:8px;border-radius:50%;background:rgba(255,255,255,.55)}
.hero-dots span:first-child{background:var(--white)}
.hero-copy{position:absolute;top:292px;left:0;right:0;text-align:center}
.hero-copy h1{font-size:42px;font-weight:400}
.hero-copy p{width:760px;margin:14px auto 0;font-size:18px;line-height:29px}
.btn-trial{display:inline-block;margin-top:26px;background:var(--orange);padding:16px 30px;font-size:13px;font-weight:700;letter-spacing:.4px}

/* About */
.about{height:885px;background:var(--dark);color:#bdbdbd}
.about .section-title{color:var(--white);padding-top:82px}
.about-text{width:960px;margin:26px auto 0;text-align:center;font-size:13.5px;line-height:27px}
.about-text p+p{margin-top:20px}
.about-panel{position:absolute;left:186px;top:346px;width:830px;height:460px;border:4px solid #1c1c1e;background:var(--teal);box-shadow:0 0 0 2px #3a3a3d}
.about-art{position:absolute;left:50px;top:40px;width:460px;height:370px;background:radial-gradient(circle at 50% 55%,#4cc3c7 0%,#2ea4aa 70%)}
.about-panel h3{position:absolute;left:536px;top:116px;font-size:44px;font-weight:400;color:var(--white)}
.about-panel p{position:absolute;left:540px;top:192px;width:220px;font-size:13px;line-height:21px;color:var(--white)}
.about-wave{position:absolute;left:0;bottom:-30px;width:1200px;height:60px}

/* Services */
.services{height:699px;background:var(--white)}
.services .section-title{padding-top:100px}
.service{position:absolute;width:470px}
.service svg{position:absolute;left:0;top:0}
.service h4{margin-left:79px;font-size:14.5px;font-weight:600;color:var(--ink)}
.service p{margin-left:79px;margin-top:10px;font-size:12.5px;line-height:21px;color:var(--muted)}

/* Pricing */
.pricing{height:822px;background:var(--light)}
.pricing .section-title{padding-top:64px}
.plans{position:absolute;left:101px;top:181px;display:flex}
.plan{width:333px;height:567px;color:var(--white);text-align:center;position:relative}
.plan-free{background:var(--free)}
.plan-standard{background:var(--standard);box-shadow:0 0 24px rgba(0,0,0,.35);z-index:1}
.plan-premium{background:var(--premium)}
.plan h3{font-size:33px;font-weight:400;margin-top:40px}
.plan-lead{font-size:18px;line-height:24px;margin-top:2px}
.plan-price{font-size:26px;margin-top:2px}
.plan-price b{font-size:54px;font-weight:400}
.plan-note{font-size:10px;line-height:15px;margin-top:8px}
.plan ul{list-style:none;position:absolute;top:224px;left:0;right:0;font-size:13.5px;line-height:33px}
.plan li{text-decoration:underline}
.plan-cta{position:absolute;left:61px;top:468px;width:210px;height:60px;border:2px solid var(--white);padding-top:8px}
.plan-cta strong{display:block;font-size:18px;font-weight:600;letter-spacing:.3px}
.plan-cta small{display:block;font-size:9.5px;margin-top:2px}

/* Testimonials */
.testimonials{height:603px;background:var(--white)}
.testimonials .section-title{padding-top:82px}
.quote-card{position:absolute;width:474px;height:168px;border:1px solid #e2e2e2;box-shadow:0 1px 4px rgba(0,0,0,.06)}
.avatar{position:absolute;left:28px;top:28px;width:90px;height:90px;border-radius:50%;background:linear-gradient(#cfcfcf,#8f8f8f)}
.quote-mark{position:absolute;font-size:32px;color:#b9b9b9;font-family:Georgia,serif;line-height:1}
.quote-card blockquote{position:absolute;left:164px;top:24px;width:270px;font-size:11.5px;line-height:19px;font-style:italic;color:#777}
.quote-card cite{position:absolute;left:164px;top:122px;font-size:11px;font-style:italic;color:#888}
.quote-card cite b{color:var(--orange);font-style:normal;font-weight:700}

/* Footer */
.site-footer{height:411px;background:var(--darker);color:#bdbdbd;font-size:12.5px}
.foot-col{position:absolute;top:82px}
.foot-col h5{font-size:14px;color:var(--white);font-weight:700;letter-spacing:.4px;padding-bottom:10px;position:relative}
.foot-col h5::after{content:"";position:absolute;left:0;bottom:0;width:44px;height:2px;background:var(--orange)}
.foot-col ul{list-style:none;margin-top:20px;line-height:33px}
.foot-about p{margin-top:20px;width:260px;line-height:21px}
.contact-list{list-style:none;margin-top:18px;line-height:33px}
.contact-list li{display:flex;align-items:center;gap:10px;font-size:11.5px}
.btn-contact{display:inline-block;margin-top:18px;border:2px solid var(--orange);color:var(--white);padding:9px 30px;font-size:12px;font-weight:700}
.copyright{position:absolute;left:0;right:0;top:336px;text-align:center;font-size:11px;color:#9a9a9a}
.copyright span{color:var(--orange)}
.to-top{position:absolute;right:42px;top:336px;font-size:11px;color:#9a9a9a}
</style>
</head>
<body>

<header class="hero">
  <div class="hero-photo" role="img" aria-label="Photo of people working at computer monitors in an office"></div>
  <div class="hero-shade"></div>
  <nav class="nav">
    <div class="brand">LoopWatch</div>
    <ul class="nav-links">
      <li>ABOUT US</li><li>SERVICES</li><li>PRICING PLAN</li><li>TESTIMONIALS</li><li>CONTACT US</li>
    </ul>
  </nav>
  <div class="hero-dots"><span></span><span></span><span></span><span></span><span></span></div>
  <div class="hero-copy">
    <h1>Website monitoring for everyone</h1>
    <p>Zentrovia makes it easy to monitor your websites and servers. Get alerts when your website is down and insights to its performance and functionality.</p>
    <span class="btn-trial">START YOUR FREE 14-DAY TRIAL</span>
  </div>
</header>

<section class="about">
  <h2 class="section-title">About LoopWatch</h2>
  <div class="about-text">
    <p>Anyone with a website knows that things can sometimes go wrong. Sometimes it is with the code, the server or the network. LoopWatch monitors your websites every minute and alerts you if your sites are down.</p>
    <p>A website can be down in various ways. It could be unreachable indicating a network problem. It could be up but throwing some sort of an error, or it could be misconfigured and not serving the correct content. Whatever the issue, LoopWatch will identify it for you.</p>
  </div>
  <div class="about-panel">
    <div class="about-art" role="img" aria-label="Illustration of clouds, browser windows, gears and users connected by dotted lines"></div>
    <h3>LoopWatch</h3>
    <p>Anyone with a website knows that things can sometimes go wrong. Sometimes it is with the code, the server or the network. LoopWatch monitors your websites every minute and alerts you if your sites are down.</p>
  </div>
  <svg class="about-wave" viewBox="0 0 1200 60" preserveAspectRatio="none" aria-hidden="true">
    <path d="M0 30 H470 C540 30 560 60 600 60 C640 60 660 30 730 30 H1200 V60 H0 Z" fill="#ffffff"/>
    <path d="M0 0 H1200 V30 H730 C660 30 640 60 600 60 C560 60 540 30 470 30 H0 Z" fill="#2b2b2e"/>
  </svg>
</section>

<section class="services">
  <h2 class="section-title">Our Services</h2>
  <p class="section-sub">Anyone with a website knows that things can sometimes go wrong.</p>

  <div class="service" style="left:99px;top:233px">
    <svg width="56" height="48" viewBox="0 0 56 48" fill="none" stroke="#f06a24" stroke-width="3"><rect x="3" y="3" width="50" height="32"/><path d="M10 26 L20 16 L28 22 L44 10"/><path d="M20 45 H36 M28 35 V45"/></svg>
    <h4>Monitoring</h4>
    <p>When your site is down it can mean lost sales, damage yo your brand, and lower search engine rankings. LoopWatch has a global network of probe servers to test your website as often as every minute.</p>
  </div>
  <div class="service" style="left:641px;top:233px">
    <svg width="56" height="48" viewBox="0 0 56 48" fill="none" stroke="#f06a24" stroke-width="3"><rect x="19" y="4" width="18" height="40" rx="3"/><path d="M12 14 Q7 24 12 34 M6 10 Q-1 24 6 38 M44 14 Q49 24 44 34 M50 10 Q57 24 50 38"/></svg>
    <h4>Alerting</h4>
    <p>When your site is down you are immediately alerted. Get alerted via e-mail, SMS, Chirpline, push, Chatly, TeamPost, AlertDesk...</p>
  </div>
  <div class="service" style="left:99px;top:379px">
    <svg width="56" height="48" viewBox="0 0 56 48" fill="#f06a24"><rect x="4" y="30" width="6" height="14"/><rect x="14" y="22" width="6" height="22"/><rect x="24" y="14" width="6" height="30"/><rect x="34" y="6" width="6" height="38"/><rect x="44" y="18" width="6" height="26"/></svg>
    <h4>Stats</h4>
    <p>View performance trends in a beautifully designed UI. View uptime, downtime and the and a breakdown of response times to help diagnose where slowness is happening.</p>
  </div>
  <div class="service" style="left:641px;top:379px">
    <svg width="56" height="48" viewBox="0 0 56 48" fill="none" stroke="#f06a24" stroke-width="4"><path d="M16 12 L4 24 L16 36 M40 12 L52 24 L40 36 M32 8 L24 40"/></svg>
    <h4>API</h4>
    <p>LoopWatch provides an easy to use API for managing checks and integrating check results into your own application.</p>
  </div>
  <div class="service" style="left:99px;top:527px">
    <svg width="56" height="48" viewBox="0 0 56 48" fill="none" stroke="#f06a24" stroke-width="3"><rect x="16" y="2" width="22" height="44" rx="3"/><path d="M16 38 H38 M24 42 H30"/></svg>
    <h4>Mobile</h4>
    <p>Managing your alerts and website checks with our mobile app couldn't be easier and you will be alerted where ever you.</p>
  </div>
</section>

<section class="pricing">
  <h2 class="section-title">Pricing Plan</h2>
  <p class="section-sub">Anyone with a website knows that things can sometimes go wrong.</p>
  <div class="plans">
    <div class="plan plan-free">
      <h3>Free plan</h3>
      <p class="plan-lead">For Website and Server<br>Monitoring.</p>
      <p class="plan-note">(paid annually)Total Monitors 10<br>Buy Add-ons for more.</p>
      <ul><li>Includes 10 Websites</li><li>1 min Poll Frequency</li><li>Includes 1 Advanced Monitor</li><li>100K RUM Pageviews</li><li>Select 8 Test Locations</li><li>50 SMS/Voice Credits Per Month</li><li>Standard Support</li></ul>
      <div class="plan-cta"><strong>SIGN UP NOW</strong><small>14 DAYS FREE TRIAL</small></div>
    </div>
    <div class="plan plan-standard">
      <h3>Standared Plan</h3>
      <p class="plan-price">$<b>102</b>/ 6 months</p>
      <p class="plan-note">(paid annually)Total Monitors 10<br>Buy Add-ons for more.</p>
      <ul><li>Includes 10 Websites</li><li>1 min Poll Frequency</li><li>Includes 1 Advanced Monitor</li><li>100K RUM Pageviews</li><li>Select 8 Test Locations</li><li>50 SMS/Voice Credits Per Month</li><li>Standard Support</li></ul>
      <div class="plan-cta"><strong>SIGN UP NOW</strong><small>FOR BUY A PLAN</small></div>
    </div>
    <div class="plan plan-premium">
      <h3>Premium Plan</h3>
      <p class="plan-price">$<b>204</b>/ 12 months</p>
      <p class="plan-note">(paid annually)Total Monitors 10<br>Buy Add-ons for more.</p>
      <ul><li>Includes 10 Websites</li><li>1 min Poll Frequency</li><li>Includes 1 Advanced Monitor</li><li>100K RUM Pageviews</li><li>Select 8 Test Locations</li><li>50 SMS/Voice Credits Per Month</li><li>Standard Support</li></ul>
      <div class="plan-cta"><strong>SIGN UP NOW</strong><small>FOR BUY A PLAN</small></div>
    </div>
  </div>
</section>

<section class="testimonials">
  <h2 class="section-title">Testimonials</h2>

  <div class="quote-card" style="left:101px;top:156px">
    <div class="avatar" role="img" aria-label="Customer portrait"></div>
    <span class="quote-mark" style="left:140px;top:20px">&ldquo;</span>
    <blockquote>Es simplemente el texto de relleno de las imprentas y archivos de texto. Lorem Ipsum ha sido el texto de relleno estándar de las industrias desde el año 1500, cuando un impresor...</blockquote>
    <span class="quote-mark" style="left:446px;top:92px">&rdquo;</span>
    <cite><b>MARLO VESTIN</b> - Business man</cite>
  </div>
  <div class="quote-card" style="left:625px;top:156px">
    <div class="avatar" role="img" aria-label="Customer portrait"></div>
    <span class="quote-mark" style="left:140px;top:20px">&ldquo;</span>
    <blockquote>Es simplemente el texto de relleno de las imprentas y archivos de texto. Lorem Ipsum ha sido el texto de relleno estándar de las industrias desde el año 1500, cuando un impresor...</blockquote>
    <span class="quote-mark" style="left:446px;top:92px">&rdquo;</span>
    <cite><b>MARLO VESTIN</b> - Business man</cite>
  </div>
  <div class="quote-card" style="left:101px;top:359px">
    <div class="avatar" role="img" aria-label="Customer portrait"></div>
    <span class="quote-mark" style="left:140px;top:20px">&ldquo;</span>
    <blockquote>Es simplemente el texto de relleno de las imprentas y archivos de texto. Lorem Ipsum ha sido el texto de relleno estándar de las industrias desde el año 1500, cuando un impresor...</blockquote>
    <span class="quote-mark" style="left:446px;top:92px">&rdquo;</span>
    <cite><b>MARLO VESTIN</b> - Business man</cite>
  </div>
  <div class="quote-card" style="left:625px;top:359px">
    <div class="avatar" role="img" aria-label="Customer portrait"></div>
    <span class="quote-mark" style="left:140px;top:20px">&ldquo;</span>
    <blockquote>Es simplemente el texto de relleno de las imprentas y archivos de texto. Lorem Ipsum ha sido el texto de relleno estándar de las industrias desde el año 1500, cuando un impresor...</blockquote>
    <span class="quote-mark" style="left:446px;top:92px">&rdquo;</span>
    <cite><b>MARLO VESTIN</b> - Business man</cite>
  </div>
</section>

<footer class="site-footer">
  <div class="foot-col foot-about" style="left:101px">
    <h5>LOOPWATCH</h5>
    <p>Es simplemente el texto de relleno de las imprentas y archivos de texto</p>
    <ul class="contact-list">
      <li><svg width="14" height="14" viewBox="0 0 14 14" fill="#ffffff"><path d="M3 1 L5 1 L6 4 L4.5 5.5 Q6 8.5 8.5 9.5 L10 8 L13 9 L13 11 Q13 13 11 13 Q2 12 1 3 Q1 1 3 1Z"/></svg>Telephone: +1 (555) 014 2290</li>
      <li><svg width="14" height="14" viewBox="0 0 14 14" fill="none" stroke="#ffffff" stroke-width="1.5"><rect x="1" y="3" width="12" height="8"/><path d="M1 3 L7 8 L13 3"/></svg>Email: info@loopwatch.com</li>
      <li><svg width="14" height="14" viewBox="0 0 14 14" fill="#ffffff"><path d="M7 1 Q2 1 2 6 Q2 9 7 13 Q12 9 12 6 Q12 1 7 1Z M7 4 A2 2 0 1 0 7.01 4Z"/></svg>120 Street name, City name, Country name 000566</li>
    </ul>
    <span class="btn-contact">CONTACT</span>
  </div>
  <div class="foot-col" style="left:510px">
    <h5>WELCOME</h5>
    <ul><li>About Us</li><li>Services</li><li>Pricing Plan</li><li>Testimonials</li><li>Contact Us</li></ul>
  </div>
  <div class="foot-col" style="left:726px">
    <h5>OUR SERVICE</h5>
    <ul><li>Monitoring</li><li>Alerting</li><li>Stats</li><li>API</li><li>Mobile</li></ul>
  </div>
  <div class="foot-col" style="left:934px">
    <h5>INFORMATION</h5>
    <ul><li>Disclaimer</li><li>Privacy &amp; Policy</li><li>Terms &amp; Conditions</li><li>Sitemap</li></ul>
  </div>
  <p class="copyright">Copyright © 2016, <span>LoopWatch</span>. All Rights Reserved.</p>
  <span class="to-top">UP</span>
</footer>

</body>
</html>
```